Postcard Design

The business Logo is 'Verdo' it is grass cutting and maintenance. It will offer grass cutting with stripes including edging. Other services include decking/fencing maintenance, lawn treatment and patio/drive cleaning...... prices start from £10 to include front and rear lawns, Regular cuts or a one off tidy. private and commercial. Contracts welcome.
call 01642583106 or 07474829150 for a free quote.
one of the pics that i have sent is the logo (obviously it would need to be tidied up and neater) that is just rough. The other pic is one of pella cards templates but is the one that is the preferred out of all of them. If it could be similar to that with the logo on would be great.
a before (long scruffy grass) and after (neat Lawn) half and half of the postcard would be great.

Target Market(s)

Middle class home owners.

Industry/Entity Type

Business

Requirements
Must have
• The 'Verdo' logo
Nice to have
• we have a lot of junk mail posted in this area and a lot just gets put in the bin so could you make it eye catching.

```html
<!DOCTYPE html>
<html lang="en">
<head>
<meta charset="utf-8">
<title>Verdo – Grass Cutting &amp; Maintenance Postcard</title>
<link href="https://fonts.googleapis.com/css2?family=Arvo:wght@700&family=Sorts+Mill+Goudy&display=swap" rel="stylesheet">
<style>
  :root {
    --backdrop: #e6e4e0;
    --lawn-light: #8fd14a;
    --lawn-mid: #5fb52e;
    --lawn-dark: #3e8f1e;
    --blade-dark: #1f4a12;
    --blade-mid: #3f7d28;
    --gravel: #d3cfc4;
    --gravel-light: #e0ddd4;
    --charcoal: #2b2b2b;
    --ink: #1e1e1e;
    --white: #ffffff;
    --brand-green: #3fae49;
    --rule-grey: #9a9a9a;
    --stamp-grey: #6d6d6d;
  }
  * { margin: 0; padding: 0; box-sizing: border-box; }
  html, body {
    width: 1200px; height: 1000px; overflow: hidden;
    background: var(--backdrop);
  }
  .canvas { position: relative; width: 1200px; height: 1000px; }

  .card {
    position: absolute;
    overflow: hidden;
    background: var(--white);
    box-shadow: 0 6px 18px rgba(0,0,0,.18);
  }

  /* ---------- Front ---------- */
  .card--front { left: 40px; top: 40px; width: 560px; height: 500px; }
  .front-art { position: absolute; inset: 0; }
  .brand-plate {
    position: absolute;
    left: 50%; top: 70px;
    transform: translateX(-50%);
    width: 260px; height: 104px;
    background: var(--white);
    border-radius: 18px;
    display: flex; align-items: center; justify-content: center;
  }
  .brand-name {
    font-family: "Arvo", Georgia, serif;
    font-weight: 700;
    font-size: 58px;
    letter-spacing: 2px;
    color: var(--ink);
  }
  .front-tagline {
    position: absolute;
    left: 0; right: 0; top: 226px;
    text-align: center;
    font-family: "Arvo", Georgia, serif;
    font-weight: 700;
    font-size: 31px;
    color: var(--white);
    text-shadow: 0 2px 3px rgba(0,0,0,.25);
  }
  .front-contact {
    position: absolute;
    left: 0; right: 0; top: 360px;
    text-align: center;
    font-family: "Sorts Mill Goudy", Georgia, serif;
    color: var(--ink);
  }
  .front-contact__phones {
    font-size: 28px;
    display: flex; align-items: center; justify-content: center; gap: 8px;
  }
  .front-contact__phones svg { width: 22px; height: 22px; }
  .front-contact__cta { font-size: 38px; line-height: 1.15; }
  .front-contact__cta strong { font-weight: 400; font-size: 44px; letter-spacing: 1px; }

  /* ---------- Back ---------- */
  .card--back { left: 460px; top: 520px; width: 700px; height: 440px; }
  .price-band {
    position: absolute; left: 0; top: 0;
    width: 540px; height: 160px;
    background:
      linear-gradient(180deg, rgba(0,0,0,0) 55%, rgba(0,0,0,.35) 100%),
      linear-gradient(100deg, var(--blade-dark) 0%, var(--blade-mid) 35%, #5a9a3a 60%, var(--blade-dark) 100%);
  }
  .brand-plate--small {
    left: 30px; top: 34px; transform: none;
    width: 132px; height: 50px; border-radius: 9px;
  }
  .brand-plate--small .brand-name { font-size: 28px; letter-spacing: 1px; }
  .price-line {
    position: absolute; left: 26px; bottom: 8px;
    font-family: "Sorts Mill Goudy", Georgia, serif;
    color: var(--white);
    font-size: 32px;
    white-space: nowrap;
  }
  .price-line__amount { font-size: 60px; vertical-align: -4px; }

  .stamp-box {
    position: absolute; right: 36px; top: 28px;
    width: 96px; height: 110px;
    border: 1.5px solid var(--rule-grey);
    display: flex; align-items: center; justify-content: center;
    text-align: center;
    font-family: "Sorts Mill Goudy", Georgia, serif;
    font-size: 16px; line-height: 1.3;
    color: var(--stamp-grey);
  }
  .address-divider {
    position: absolute; left: 400px; top: 178px;
    width: 1.5px; height: 230px;
    background: var(--rule-grey);
  }
  .services {
    position: absolute; left: 24px; top: 178px; width: 330px;
    text-align: center;
    font-family: "Sorts Mill Goudy", Georgia, serif;
    color: var(--ink);
  }
  .services__headline {
    font-weight: 400;
    font-size: 21px; line-height: 1.05;
    color: var(--brand-green);
    text-transform: uppercase;
    margin-bottom: 14px;
  }
  .services__list { list-style: none; font-size: 17px; line-height: 1.3; }
  .services__list li::before { content: "• "; }
</style>
</head>
<body>
<main class="canvas">

  <section class="card card--front" aria-label="Postcard front">
    <svg class="front-art" viewBox="0 0 560 500" preserveAspectRatio="none">
      <defs>
        <linearGradient id="lawnGrad" x1="0" y1="0" x2="1" y2="1">
          <stop offset="0" stop-color="var(--lawn-mid)"/>
          <stop offset=".3" stop-color="var(--lawn-light)"/>
          <stop offset=".6" stop-color="var(--lawn-mid)"/>
          <stop offset="1" stop-color="var(--lawn-dark)"/>
        </linearGradient>
        <linearGradient id="gravelGrad" x1="0" y1="0" x2="0" y2="1">
          <stop offset="0" stop-color="var(--gravel-light)"/>
          <stop offset="1" stop-color="var(--gravel)"/>
        </linearGradient>
      </defs>
      <rect width="560" height="500" fill="url(#lawnGrad)" role="img" aria-label="Freshly mown striped lawn"/>
      <path d="M0,400 Q170,300 560,296 L560,500 L0,500 Z" fill="var(--charcoal)"/>
      <path d="M0,410 Q170,310 560,306 L560,500 L0,500 Z" fill="url(#gravelGrad)"/>
    </svg>

    <div class="brand-plate"><span class="brand-name">VERDO</span></div>
    <p class="front-tagline">Grass Cutting &amp; Maintenance</p>

    <div class="front-contact">
      <p class="front-contact__phones">
        <svg viewBox="0 0 24 24" aria-hidden="true"><circle cx="12" cy="12" r="10.5" fill="none" stroke="var(--ink)" stroke-width="1.5"/><path d="M8.5 6.5l2 2-1.2 1.6c.8 1.7 2 2.9 3.6 3.6l1.6-1.2 2 2-1.3 1.8c-4-.6-7.7-4.3-8.3-8.3z" fill="var(--ink)"/></svg>
        01642583106 or 07474829150
      </p>
      <p class="front-contact__cta">for a <strong>FREE</strong> quote</p>
    </div>
  </section>

  <section class="card card--back" aria-label="Postcard back">
    <div class="price-band" role="img" aria-label="Close-up of long green grass blades">
      <div class="brand-plate brand-plate--small"><span class="brand-name">VERDO</span></div>
      <p class="price-line">Prices starting from <span class="price-line__amount">£10</span></p>
    </div>

    <div class="stamp-box">Affix<br>Postage</div>

    <div class="services">
      <h2 class="services__headline">We offer grass<br>cutting with stripes<br>including edging.</h2>
      <ul class="services__list">
        <li>Front and rear lawns.</li>
        <li>Other services include decking/fencing maintenance, lawn treatment and patio/drive cleaning.</li>
        <li>Regular cuts or a one-off tidy.</li>
        <li>Private and commercial contracts welcome.</li>
      </ul>
    </div>

    <div class="address-divider"></div>
  </section>

</main>
</body>
</html>
```